Diagram of Marrowfen’s history for website

This project is to design the attached diagram along the lines of the attached image but in our branding - style guide attached. The diagram will be going on the Marrowfen website - www.marrowfen.au.

```html
<!DOCTYPE html>
<html lang="en">
<head>
<meta charset="utf-8">
<title>Our History – Marrowfen</title>
<link href="https://fonts.googleapis.com/css2?family=Poppins:wght@400;500;700&display=swap" rel="stylesheet">
<style>
  :root {
    --ink: #3a3a3c;
    --teal: #7f9ea3;
    --sage: #6e8f74;
    --clay: #d4ab96;
    --paper: #ffffff;
  }
  * { margin: 0; padding: 0; box-sizing: border-box; }
  html, body { width: 1200px; height: 849px; overflow: hidden; background: var(--paper); }
  .history {
    position: relative;
    width: 1200px;
    height: 849px;
    font-family: "Poppins", sans-serif;
    color: var(--ink);
  }
  .timeline-art { position: absolute; inset: 0; }
  .title {
    position: absolute;
    left: 80px;
    top: 70px;
    font-size: 59px;
    line-height: 1;
    font-weight: 700;
    letter-spacing: -1px;
    color: var(--ink);
  }
  .year {
    position: absolute;
    font-size: 37px;
    line-height: 1;
    font-weight: 700;
    letter-spacing: -0.5px;
    color: var(--sage);
  }
  .event { position: absolute; white-space: nowrap; }
  .event-title {
    font-size: 18.5px;
    line-height: 24px;
    font-weight: 500;
    color: var(--teal);
  }
  .event-text {
    font-size: 14.5px;
    line-height: 20px;
    font-weight: 400;
    color: var(--ink);
  }
  .event-text.loose { line-height: 23px; }
</style>
</head>
<body>
<main class="history">
  <svg class="timeline-art" width="1200" height="849" viewBox="0 0 1200 849" aria-hidden="true">
    <g stroke="var(--clay)" stroke-width="5" fill="none">
      <line x1="57" y1="456" x2="57" y2="706"/>
      <line x1="209" y1="456" x2="209" y2="287"/>
      <line x1="362" y1="456" x2="362" y2="552"/>
      <line x1="515" y1="456" x2="515" y2="267"/>
      <line x1="667" y1="456" x2="667" y2="718"/>
      <line x1="820" y1="456" x2="820" y2="55"/>
    </g>
    <line x1="57" y1="456" x2="1134" y2="456" stroke="var(--clay)" stroke-width="8"/>
    <polygon points="1130,435 1168,456 1130,477" fill="var(--clay)"/>
    <g fill="var(--sage)">
      <circle cx="57" cy="456" r="16"/>
      <circle cx="209" cy="456" r="16"/>
      <circle cx="362" cy="456" r="16"/>
      <circle cx="515" cy="456" r="16"/>
      <circle cx="667" cy="456" r="16"/>
      <circle cx="820" cy="456" r="16"/>
    </g>
    <g fill="var(--teal)">
      <circle cx="57" cy="552" r="10.5"/>
      <circle cx="57" cy="706" r="10.5"/>
      <circle cx="209" cy="287" r="10.5"/>
      <circle cx="362" cy="552" r="10.5"/>
      <circle cx="515" cy="267" r="10.5"/>
      <circle cx="667" cy="552" r="10.5"/>
      <circle cx="667" cy="646" r="10.5"/>
      <circle cx="667" cy="718" r="10.5"/>
      <circle cx="820" cy="55" r="10.5"/>
      <circle cx="820" cy="108" r="10.5"/>
      <circle cx="820" cy="182" r="10.5"/>
      <circle cx="820" cy="255" r="10.5"/>
      <circle cx="820" cy="328" r="10.5"/>
    </g>
  </svg>

  <h1 class="title">Our History</h1>

  <p class="year" style="left:88px;top:486px">2017</p>
  <p class="year" style="left:240px;top:392px">2018</p>
  <p class="year" style="left:393px;top:486px">2019</p>
  <p class="year" style="left:545px;top:392px">2021</p>
  <p class="year" style="left:698px;top:486px">2022</p>
  <p class="year" style="left:850px;top:392px">2023</p>

  <section class="event" style="left:88px;top:540px">
    <h2 class="event-title">Marrowfen Commences</h2>
    <p class="event-text">Maren started the business<br>with 25 years’ experience<br>working for government &amp; non-<br>government disability &amp;<br>community services. Our first<br>office is in Ashby</p>
  </section>
  <section class="event" style="left:88px;top:694px">
    <h2 class="event-title">NCAS Provider</h2>
    <p class="event-text">Marrowfen becomes a NCAS<br>Registered provider</p>
  </section>

  <section class="event" style="left:240px;top:275px">
    <h2 class="event-title">Clinic Expansion</h2>
    <p class="event-text">Marrowfen moves offices<br>twice in Ashby due to<br>growth &amp; expansion. Clinic<br>established</p>
  </section>

  <section class="event" style="left:393px;top:540px">
    <h2 class="event-title">Move to Elderwood</h2>
    <p class="event-text">Marrowfen moves to<br>Elderwood due to further<br>growth &amp; expansion</p>
  </section>

  <section class="event" style="left:545px;top:255px">
    <h2 class="event-title">Civic-Corporation</h2>
    <p class="event-text">Marrowfen becomes a<br>accredited Civic-Corporation<br>having met the highest<br>standards of environmental,<br>social &amp; community performance</p>
  </section>

  <section class="event" style="left:698px;top:540px">
    <h2 class="event-title">Veltra Best of Business</h2>
    <p class="event-text">Marrowfen wins the Veltra<br>Best of Business Award (North)<br>for building communities</p>
  </section>
  <section class="event" style="left:698px;top:634px">
    <h2 class="event-title">Move to Halden</h2>
    <p class="event-text loose">Marrowfen moves to a larger<br>premises in Halden</p>
  </section>
  <section class="event" style="left:698px;top:706px">
    <h2 class="event-title">Partnerships</h2>
    <p class="event-text">Partnerships established with<br>Kestrel Bay School for Children with<br>Disability &amp; Tallow Creek Centre<br>(Northgate University)</p>
  </section>

  <section class="event" style="left:850px;top:43px">
    <h2 class="event-title">Rebranding</h2>
    <p class="event-text">Marrowfen rebranded</p>
  </section>
  <section class="event" style="left:850px;top:96px">
    <h2 class="event-title">Community Action Plan (CAP)</h2>
    <p class="event-text">Marrowfen’s Foundation CAP<br>developed &amp; endorsed</p>
  </section>
  <section class="event" style="left:850px;top:170px">
    <h2 class="event-title">Client Advisory Group</h2>
    <p class="event-text">Marrowfen’s Client Advisory Group<br>commences</p>
  </section>
  <section class="event" style="left:850px;top:243px">
    <h2 class="event-title">E-Learning Platform</h2>
    <p class="event-text">Marrowfen e-learning platform<br>launched</p>
  </section>
  <section class="event" style="left:850px;top:316px">
    <h2 class="event-title">Spectrum Tick</h2>
    <p class="event-text">Marrowfen achieves Spectrum Tick<br>accreditation</p>
  </section>
</main>
</body>
</html>
```